Business Card Design

Quorvel Software Limited develops and sells venue and event management software called Quorvel Stagehand, which is available in the cloud or on-premise. The company was established in 1986. Most of our customers are performing arts venues, museums and festivals. Our existing design is a bit dull. We need to convey that we are both innovative and reliable.
Not all our people show their mobile phone numbers on their cards, so the design needs to work land line and mobile or land line only.

Industry/Entity Type

Software

Contact Information for Business Card

Helen Brackwood
Director
Quorvel Software Limited
42B Millbank Lane, Epsom, Surrey, KT19 3DW
Telephone: +44 (0)1372 904213
Mobile: +44 (0)7700 900562
Email: hbrackwood@quorvel.example
Web: www.quorvel.example

```html
<!DOCTYPE html>
<html lang="en">
<head>
<meta charset="utf-8">
<title>Quorvel Software Limited – Business Card</title>
<link href="https://fonts.googleapis.com/css2?family=Didact+Gothic&family=Poppins:wght@600;700&display=swap" rel="stylesheet">
<style>
  :root {
    --navy: #03284a;
    --mid-blue: #0b5ea8;
    --deep-blue: #053a6b;
    --grey: #c3c5cb;
    --paper: #ffffff;
    --stage: #eceef0;
    --link-blue: #1a6fc0;
  }
  * { box-sizing: border-box; margin: 0; padding: 0; }
  html, body { width: 1200px; height: 720px; overflow: hidden; }
  body {
    background: var(--stage);
    font-family: "Didact Gothic", "Century Gothic", sans-serif;
    position: relative;
  }
  .card {
    position: absolute;
    top: 192px;
    width: 520px;
    height: 336px;
    overflow: hidden;
    box-shadow: 0 2px 10px rgba(0,0,0,0.12);
  }
  .card svg.card-art { position: absolute; inset: 0; }

  /* Back of card */
  .card-back { left: 50px; background: var(--navy); }
  .card-back .tagline {
    position: absolute;
    right: 40px;
    top: 120px;
    text-align: right;
    color: #e8ebf0;
  }
  .card-back .tagline-text { font-size: 17px; letter-spacing: 0.3px; }
  .card-back .tagline-url {
    margin-top: 8px;
    font-family: "Poppins", sans-serif;
    font-weight: 600;
    font-size: 17px;
    letter-spacing: 0.6px;
  }

  /* Front of card */
  .card-front { left: 630px; background: var(--paper); }
  .brand {
    position: absolute;
    left: 34px;
    top: 62px;
    display: flex;
    align-items: center;
    gap: 12px;
  }
  .brand-square { width: 22px; height: 22px; background: var(--deep-blue); }
  .brand-name {
    font-family: "Poppins", sans-serif;
    font-weight: 700;
    font-size: 24px;
    letter-spacing: 1.5px;
    color: var(--deep-blue);
  }
  .contact {
    position: absolute;
    right: 26px;
    top: 54px;
    width: 200px;
    text-align: right;
    color: #ffffff;
  }
  .person-name {
    font-family: "Poppins", sans-serif;
    font-weight: 600;
    font-size: 20px;
    line-height: 1.1;
    white-space: nowrap;
  }
  .person-title { font-size: 14px; margin-top: 3px; }
  .company { color: var(--link-blue); font-size: 14px; margin-top: 24px; white-space: nowrap; }
  .details { list-style: none; margin-top: 10px; font-size: 12.5px; }
  .details li {
    display: flex;
    justify-content: flex-end;
    align-items: flex-start;
    gap: 8px;
    line-height: 1.35;
    margin-bottom: 3px;
    white-space: nowrap;
  }
  .details svg { flex: none; width: 12px; height: 12px; margin-top: 3px; }
</style>
</head>
<body>

<section class="card card-back" aria-label="Card back">
  <svg class="card-art" viewBox="0 0 520 336" aria-hidden="true">
    <polygon points="0,230 260,336 0,336" fill="var(--deep-blue)"/>
    <polygon points="0,280 140,336 0,336" fill="var(--mid-blue)"/>
    <rect x="0" y="0" width="14" height="336" fill="var(--grey)"/>
  </svg>
  <div class="tagline">
    <p class="tagline-text">Event And Venue Management Software</p>
    <p class="tagline-url">www.quorvel.example</p>
  </div>
</section>

<section class="card card-front" aria-label="Card front">
  <svg class="card-art" viewBox="0 0 520 336" aria-hidden="true">
    <path d="M285,0 C245,60 234,200 247,336 L262,336 C250,200 260,60 300,0 Z" fill="var(--grey)"/>
    <path d="M300,0 C260,60 250,200 262,336 L520,336 L520,0 Z" fill="var(--navy)"/>
  </svg>

  <div class="brand">
    <span class="brand-square"></span>
    <span class="brand-name">QUORVEL</span>
  </div>

  <div class="contact">
    <p class="person-name">Helen Brackwood</p>
    <p class="person-title">Director</p>
    <p class="company">Quorvel Software Limited</p>
    <ul class="details">
      <li><span>hbrackwood@quorvel.example</span>
        <svg viewBox="0 0 12 12"><rect x="0.5" y="2" width="11" height="8" fill="none" stroke="#fff"/><path d="M0.5 2 L6 6.5 L11.5 2" fill="none" stroke="#fff"/></svg></li>
      <li><span>+44 (0)7700 900562</span>
        <svg viewBox="0 0 12 12"><rect x="3" y="0.5" width="6" height="11" rx="1" fill="none" stroke="#fff"/><rect x="4.2" y="2" width="3.6" height="5" fill="#fff"/></svg></li>
      <li><span>+44 (0)1372 904213</span>
        <svg viewBox="0 0 12 12"><path d="M1 5 Q6 1 11 5 L11 6.5 L8.5 6.5 L8 5 Q6 4.2 4 5 L3.5 6.5 L1 6.5 Z" fill="#fff"/><rect x="3" y="7.5" width="6" height="3.5" fill="#fff"/></svg></li>
      <li><span>42B Millbank Lane, Epsom,<br>Surrey, KT19 3DW</span>
        <svg viewBox="0 0 12 12"><path d="M6 11.5 L2.2 6 A4.2 4.2 0 1 1 9.8 6 Z" fill="#fff"/><circle cx="6" cy="4.3" r="1.5" fill="var(--navy)"/></svg></li>
    </ul>
  </div>
</section>

</body>
</html>
```